Fatigued and Overloaded by COVID Messages? We need original illustrations to show that.

Everywhere you look there are messages about COVID. That is leading many people to feel fatigued and overloaded by the messages.

We surveyed U.S. adults March 20th - 24th, 2020 and measured message fatigue, information overload, perceived repetition, and perceived exaggeration. Here is how participants responded:

When it comes to coronavirus . . .
55% feel exhausted by all the messages.
54% feel overloaded by the amount of information.
51% feel that the messages are repetitive.
47% feel like messages exaggerate how bad it is.

In other words, almost half of U.S. adults show signs of message fatigue, information overload, perceived message repetition, and perceived message exaggeration.

We will continue to survey 400 adults every week for the next 16 weeks. Each time we will measure message fatigue, information overload, perceived repetition, and perceived exaggeration. We expect that it will increase over time.

What are we looking for? We need innovative and original illustrations that attempt to communicate these findings. The illustrations would visualize message fatigue, information overload, perceived message repetition, and perceived message exaggeration.

What sort of visual are we looking for? Our preference is for an original illustration (or set of illustrations). Our preference is for creative and powerful illustrations, but we are also open to the creative and well-executed infographics.

We need these images fast . We will award monetary prizes to the 3 best designs. If we like more than that, then we might purchase more (e.g., in past contests, we have purchased as many as 30 designs).

What we will need:
(1) The illustrations must be original and we will need the photoshop and/or illustrator files for all artwork. (By original, we mean that the illustrations are 100% created by you. Our organization requires that we utilize only original illustrated work. We have had issues with free imagery being pirated and reposted as free. We sidestep that issue by just having everything created.)

(2) The illustration should say, somewhere: "Based on a survey of 400 U.S. adults conducted March 20 - 24th, 2020."

(3) We will have almost 4 months worth of data by the time this is done. In other words, the illustrations might be able to help us present that weekly data.

(4) We have conducted other Artvendo projects. It might be helpful to examine designs we liked in the past. For example, here is another COVID project we just finished:

https://jobs.artvendo-example.com/job/5162048

Target Market(s)

U.S. adults

Requirements
Must have
• Original illustrations. Mobile friendly design. People will view this on their smartphones.
Nice to have
• A design that we can use to communicate the data across time.

```html
<!DOCTYPE html>
<html lang="en">
<head>
<meta charset="utf-8">
<title>When It Comes to Coronavirus</title>
<link rel="stylesheet" href="https://fonts.googleapis.com/css2?family=Anton&family=Montserrat:wght@500;600;800&family=Oswald:wght@600&display=swap">
<style>
  :root {
    --mint: #a9ddd5;
    --navy: #1f3a68;
    --red: #b3202f;
    --white: #ffffff;
    --light-grey: #e4e6ea;
    --green: #7cb542;
    --illus-navy: #2b4675;
    --illus-red: #a82433;
  }
  html, body { margin: 0; padding: 0; overflow: hidden; }
  body { width: 848px; height: 1200px; background: var(--mint); font-family: "Montserrat", sans-serif; }
  .poster { position: relative; width: 848px; height: 1200px; overflow: hidden; background: var(--mint); }
  .header-art, .footer-band { position: absolute; left: 0; }
  .header-art { top: 0; width: 848px; height: 250px; }
  .footer-band { top: 1050px; width: 848px; height: 150px; }

  .title-lead {
    position: absolute; top: 46px; left: 0; width: 848px; text-align: center;
    font-family: "Montserrat", sans-serif; font-weight: 800; font-size: 52px; line-height: 1; letter-spacing: 2px;
    color: var(--green); -webkit-text-stroke: 1.5px var(--navy); margin: 0;
  }
  .title-main {
    position: absolute; top: 94px; left: 0; width: 848px; text-align: center;
    font-family: "Anton", sans-serif; font-size: 112px; line-height: 1; letter-spacing: 2px;
    color: var(--light-grey); -webkit-text-stroke: 3px var(--red); margin: 0;
  }

  .stat { position: absolute; height: 86px; }
  .stat-pill {
    position: absolute; inset: 0; background: var(--white);
    border: 4px solid var(--navy); border-radius: 43px; box-sizing: border-box;
  }
  .stat-tab {
    position: absolute; top: 10px; height: 66px; border-radius: 33px;
    display: flex; align-items: center; box-sizing: border-box;
  }
  .stat-tab p { margin: 0; color: var(--white); font-size: 15px; line-height: 1.3; font-weight: 500; text-align: center; width: 100%; }
  .stat-tab--right { background: linear-gradient(90deg, var(--red), var(--navy) 45%); }
  .stat-tab--left { background: linear-gradient(90deg, var(--navy) 40%, var(--red)); }
  .stat-figure {
    position: absolute; top: -22px; width: 130px; height: 130px; border-radius: 50%;
    background: radial-gradient(circle, var(--navy) 35%, var(--red) 100%);
    border: 5px solid var(--navy); box-sizing: border-box;
    display: flex; align-items: center; justify-content: center;
    font-family: "Oswald", sans-serif; font-weight: 600; font-size: 50px; color: var(--white);
  }

  .illustration { position: absolute; border-radius: 18px; }
  .illus-desk { left: 613px; top: 335px; width: 200px; height: 158px; background: linear-gradient(160deg, var(--illus-navy), var(--illus-red)); }
  .illus-papers { left: 22px; top: 492px; width: 220px; height: 185px; background: linear-gradient(160deg, #eef2f4, #c9d3db); }
  .illus-crouch { left: 598px; top: 627px; width: 222px; height: 214px; background: linear-gradient(160deg, var(--illus-navy), var(--illus-red)); }
  .illus-shrug { left: 57px; top: 848px; width: 185px; height: 178px; background: linear-gradient(160deg, var(--illus-red), var(--illus-navy)); }

  .survey-note {
    position: absolute; top: 1128px; left: 0; width: 848px; text-align: center; margin: 0;
    font-size: 18px; font-weight: 500; color: var(--white); line-height: 1.45;
  }
  .survey-note .survey-dates { color: var(--green); font-weight: 600; }
</style>
</head>
<body>
<main class="poster">
  <svg class="header-art" viewBox="0 0 848 250">
    <defs>
      <linearGradient id="flagTone" x1="0" y1="0" x2="1" y2="1">
        <stop offset="0" stop-color="#1f3a68"/>
        <stop offset="0.35" stop-color="#b3202f"/>
        <stop offset="0.6" stop-color="#e9e9ee"/>
        <stop offset="1" stop-color="#b3202f"/>
      </linearGradient>
    </defs>
    <path role="img" aria-label="American flag backdrop behind the title" d="M0 0 H848 V205 Q424 250 0 205 Z" fill="url(#flagTone)"/>
    <path d="M0 205 Q424 250 848 205" fill="none" stroke="#1f3a68" stroke-width="5"/>
  </svg>

  <p class="title-lead">WHEN IT COMES TO</p>
  <h1 class="title-main">CORONAVIRUS . . .</h1>

  <section class="stat" style="left:64px; top:356px; width:527px;">
    <div class="stat-pill"></div>
    <div class="stat-tab stat-tab--right" style="left:250px; width:340px; padding-left:110px;"><p>feel exhausted<br>by all the<br>messages.</p></div>
    <div class="stat-figure" style="left:199px;">55%</div>
  </section>
  <div class="illustration illus-desk" role="img" aria-label="Illustration of an exhausted person slumped over a desk"></div>

  <section class="stat" style="left:249px; top:527px; width:532px;">
    <div class="stat-pill"></div>
    <div class="stat-tab stat-tab--left" style="left:-8px; width:300px; padding-left:40px; padding-right:60px;"><p>feel overloaded<br>by the amount<br>of information.</p></div>
    <div class="stat-figure" style="left:235px;">54%</div>
  </section>
  <div class="illustration illus-papers" role="img" aria-label="Illustration of a person buried under flying papers"></div>

  <section class="stat" style="left:64px; top:705px; width:523px;">
    <div class="stat-pill"></div>
    <div class="stat-tab stat-tab--right" style="left:230px; width:356px; padding-left:120px;"><p>feel that the<br>messages are<br>repetitive.</p></div>
    <div class="stat-figure" style="left:177px;">51%</div>
  </section>
  <div class="illustration illus-crouch" role="img" aria-label="Illustration of a distressed person crouched holding their knees"></div>

  <section class="stat" style="left:249px; top:881px; width:532px;">
    <div class="stat-pill"></div>
    <div class="stat-tab stat-tab--left" style="left:-8px; width:300px; padding-left:40px; padding-right:60px;"><p>feel like messages<br>exaggerate how<br>bad it is.</p></div>
    <div class="stat-figure" style="left:235px;">47%</div>
  </section>
  <div class="illustration illus-shrug" role="img" aria-label="Illustration of a frustrated person throwing up their hands"></div>

  <svg class="footer-band" viewBox="0 0 848 150" aria-hidden="true">
    <defs>
      <linearGradient id="footerTone" x1="0" y1="0" x2="1" y2="0">
        <stop offset="0" stop-color="#1f3a68"/>
        <stop offset="0.5" stop-color="#b3202f"/>
        <stop offset="1" stop-color="#1f3a68"/>
      </linearGradient>
    </defs>
    <path d="M0 75 Q424 10 848 75 V150 H0 Z" fill="url(#footerTone)"/>
  </svg>

  <p class="survey-note">Based on a survey of 400 U.S. adults conducted<br><span class="survey-dates">March 20th - 24th, 2020.</span></p>
</main>
</body>
</html>
```